Photography and Videography - Brightwell Studios - New Business Card Design

Brightwell Studios is a photography and Videography Company started by creative couple Robby K and Lenna P and based on the Sunshine Coast in Queensland, Australia.
We're quirky, creative and innovative people and would like a business card that keeps you looking for more than just a few seconds.
Design wise we would like a black or charcoal background with a bit of a funkier design than just a boring old rectangle shape. Perhaps curved on an edge.
Ideally we would like to be able to make a collage of all of our best photos on the reverse side of the card with the company name or logo and "catch you round the bend..." (possibly in italics) underneath it.
On the front of the business card we would like our company name -
"Brightwell Studios", our motto- "Bringing Ideas To Life..." (possibly in italics) and our contact information. The background should be a darker colour like black or charcoal.
We like the look of having contact company details and contact info to one side (right) and a black and white photo of Robby K and Lenna P to the other side (left).
Thank you and Good Luck!
Industry/Entity Type
Business
Contact Information for Business Card
Business Name - Brightwell Studios
Slogan - Bring Ideas To life
Name - Robby K | Lenna P
Description - Photography | Videography
Phone - 0438 526 017 | 0412 873 205
Email - brightwellstudios@mailbox.com.au
Website - www.brightwellstudios.com.au
Logo styles of interest
Pictorial/Combination Logo
Look and feel

```html
<!DOCTYPE html>
<html lang="en">
<head>
<meta charset="utf-8">
<title>Brightwell Studios – Business Card</title>
<link rel="stylesheet" href="https://fonts.googleapis.com/css2?family=Arimo:wght@700&family=Open+Sans:wght@300;600;700&family=Crimson+Text:wght@400&display=swap">
<style>
  :root {
    --card-bg-centre: #2b2b2b;
    --card-bg-edge: #000000;
    --ink-white: #ffffff;
    --accent-green: #7dc242;
    --accent-red: #e3232b;
    --badge-fill: #e4e7ee;
    --badge-edge: #b9bfcc;
  }
  html, body {
    margin: 0;
    padding: 0;
    width: 1200px;
    height: 693px;
    overflow: hidden;
    background: #000;
  }
  .card {
    position: relative;
    width: 1200px;
    height: 693px;
    overflow: hidden;
    background: radial-gradient(ellipse 70% 75% at 50% 30%, var(--card-bg-centre) 0%, #141414 55%, var(--card-bg-edge) 100%);
    color: var(--ink-white);
  }
  .brand {
    position: absolute;
    left: 80px;
    top: 92px;
    display: flex;
    align-items: center;
    gap: 18px;
  }
  .brand-dot {
    width: 40px;
    height: 40px;
    border-radius: 50%;
    background: var(--ink-white);
  }
  .brand-name {
    font-family: "Open Sans", sans-serif;
    font-weight: 600;
    font-size: 42px;
    line-height: 1;
    color: var(--ink-white);
    white-space: nowrap;
  }
  .owners {
    position: absolute;
    right: 54px;
    top: 236px;
    text-align: right;
  }
  .owners-names {
    font-family: "Arimo", sans-serif;
    font-weight: 700;
    font-size: 56px;
    line-height: 1;
    color: var(--accent-green);
    white-space: nowrap;
  }
  .owners-services {
    margin-top: 8px;
    font-family: "Open Sans", sans-serif;
    font-weight: 300;
    font-size: 25px;
    color: var(--ink-white);
    letter-spacing: 0.5px;
    white-space: nowrap;
  }
  .contacts {
    position: absolute;
    left: 98px;
    top: 316px;
    margin: 0;
    padding: 0;
    list-style: none;
    font-family: "Crimson Text", serif;
    font-size: 30px;
    color: var(--ink-white);
  }
  .contacts li {
    height: 75px;
    display: flex;
    align-items: baseline;
    white-space: nowrap;
  }
  .contact-key {
    font-family: "Open Sans", sans-serif;
    font-weight: 700;
    font-size: 34px;
    color: var(--accent-red);
    margin-right: 10px;
  }
  .social {
    position: absolute;
    left: 98px;
    top: 536px;
    display: flex;
    align-items: center;
    gap: 16px;
    font-family: "Crimson Text", serif;
    font-size: 30px;
    color: var(--ink-white);
    white-space: nowrap;
  }
  .social-badge {
    width: 108px;
    height: 41px;
    border-radius: 6px;
    background: var(--badge-fill);
    border: 1px solid var(--badge-edge);
  }
</style>
</head>
<body>
  <main class="card">
    <div class="brand">
      <span class="brand-dot"></span>
      <span class="brand-name">Brightwell Studios</span>
    </div>

    <section class="owners">
      <div class="owners-names">Robby K | Lenna P</div>
      <div class="owners-services">Photography | Videography</div>
    </section>

    <ul class="contacts">
      <li><span class="contact-key">P</span>- 0438 526 017 &nbsp;|&nbsp; 0412 873 205</li>
      <li><span class="contact-key">E</span>- brightwellstudios@mailbox.com.au</li>
      <li><span class="contact-key">W</span>- www.brightwellstudios.com.au</li>
    </ul>

    <div class="social">
      <span>Like us on FRIENDLINE</span>
      <span class="social-badge" aria-hidden="true"></span>
    </div>
  </main>
</body>
</html>
```